Startup Technology Consulting Firm in NYC Needs A Website

I need a website built for my startup technology consulting company Larkspur Systems Group. We offer a unique white glove service that provides end to end technology support. I want to stand out above the rest. We are small firm but are very dedicated which where we derive our name from LSG primarily offers
end to end technology advisory services to small businesses lacking their own IT staff. We offer top notch white glove and our customer service and satisfaction is exceed by no one.

Below are some of what we provide our clients

Strategic IT Planning
Business Continuity Planning/Disaster Recovery
Cloud Computing\DataCenter Solutions
Server Infrastructure/Networking
Virtualization Technologies
Project Management

Our Technology Advisors hold many certifications from Quorvane & Zelpix. We are also Quorvane Partners

I have attached my logo (preview design) As soon as I ge the final images I will upload.

Industry/Entity Type

Information Technology

Coding

Coded - Design and coding required

Number of Pages Required

1 page

Font styles to use
Sans Serif

Requirements
Must have
• Attract Target Market. The site should bleed the company vision
• DEDICATION everything about the site should show this
• Layout the Benefits of our offerings
• Links to my social media
• Links to dircct my client's for remote support

```html
<!DOCTYPE html>
<html lang="en">
<head>
<meta charset="utf-8">
<title>Larkspur Systems Group</title>
<link rel="stylesheet" href="https://fonts.googleapis.com/css2?family=Raleway:wght@300;400&family=Roboto+Condensed:wght@400;700&family=Open+Sans:wght@400;600&display=swap">
<style>
:root{
  --blue:#1a6fc4;
  --blue-light:#2f8fd8;
  --navy:#123a6b;
  --ink:#333;
  --muted:#9a9a9a;
  --rule:#d9d9d9;
  --band-grey:#f6f6f6;
  --band-warm:#f2f1ee;
  --band-soft:#fafafa;
  --q-navy:#1b3d7a;
  --q-blue:#1c5fa8;
  --q-sky:#27a0d8;
  --q-light:#4db8ea;
  --z-dark:#111;
  --z-grey:#7b7b7b;
}
*{box-sizing:border-box;margin:0;padding:0}
html,body{width:682px;height:1200px;overflow:hidden;background:#fff}
body{font-family:"Open Sans",sans-serif;color:var(--ink)}
.page{position:relative;width:682px;height:1200px;overflow:hidden}
.abs{position:absolute}
.band{position:absolute;left:0;width:682px}
.center{left:0;width:682px;text-align:center}
.title{font-family:"Raleway",sans-serif;font-weight:400;font-size:11.5px;color:#333;letter-spacing:.3px}
.title.wide{letter-spacing:1.4px}
.title.blue{color:var(--blue-light)}
.kicker{font-family:"Roboto Condensed",sans-serif;font-weight:700;font-size:6.8px;color:var(--blue)}
.kick-rule{position:absolute;left:324px;width:34px;height:1px;background:var(--rule)}

/* benefits */
.product-photo{left:112px;top:22px;width:156px;height:196px;
  background:radial-gradient(ellipse 48% 50% at 52% 46%,#b07a55 0%,#c9a58c 34%,#e4dcd6 62%,#ffffff 100%)}
.benefits-title{left:318px;top:12px;font-family:"Raleway",sans-serif;font-weight:300;font-size:16px;color:var(--blue-light)}
.benefits-sub{left:319px;top:36px;font-family:"Roboto Condensed",sans-serif;font-weight:700;font-size:7.6px;color:#333}
.benefits-copy{left:319px;top:57px;width:222px}
.benefits-copy p{font-size:4.5px;line-height:8.4px;color:var(--muted);margin-bottom:8.4px}
.btn{position:absolute;display:flex;align-items:center;justify-content:center;color:#fff;font-size:5.6px}
.btn-read{left:319px;top:204px;width:62px;height:16px;background:var(--blue)}

/* clients */
.client{position:absolute;width:64px;height:27px;border-bottom:1px solid #e6e6e6;
  display:flex;align-items:center;justify-content:center;gap:4px;
  font-family:"Open Sans",sans-serif;font-weight:600;font-size:6.6px;letter-spacing:.8px;color:#444}
.client .dot{width:6px;height:6px;border-radius:50%;background:var(--blue)}

/* certificates */
.badge{position:absolute;top:414px;width:67px;height:54px}

/* contact */
.contact{position:absolute;top:548px;width:120px;text-align:center}
.contact svg{display:block;margin:0 auto}
.contact h3{font-family:"Raleway",sans-serif;font-weight:400;font-size:8.6px;color:var(--blue);margin-top:14px}
.contact p{font-size:5.4px;line-height:10px;color:#444;margin-top:1px}

/* form */
.field{position:absolute;border:1px solid #cfcfcf;background:#fff;font-size:4.6px;color:#aaa;padding:3px 3px}
.btn-submit{left:311px;top:766px;width:58px;height:16px;background:var(--navy)}

/* map */
.map{left:0;top:798px;width:682px;height:180px;
  background:linear-gradient(120deg,#e6e6e6 0%,#eeeaea 40%,#f3e3e6 70%,#ebe7e8 100%)}

/* social */
.social{position:absolute;top:1034px;width:46px;text-align:center;border-bottom:1px solid #cfcfcf;padding-bottom:3px}
.social .mark{width:5px;height:5px;border-radius:50%;background:#222;margin:0 auto 6px}
.social span{font-size:5.6px;letter-spacing:.5px;color:#555}
.btn-hello{left:311px;top:1073px;width:58px;height:17px;background:var(--navy);font-weight:600;font-size:5.6px}
.legal{top:1110px;font-size:4.6px;color:#555}
.brand{top:1131px;display:flex;flex-direction:column;align-items:center}
.brand .globe{width:26px;height:26px;border-radius:50%;background:#c4d8ec}
.brand .name{font-family:"Open Sans",sans-serif;font-weight:400;font-size:7.4px;letter-spacing:.6px;color:var(--navy);margin-top:3px}
.to-top{top:1183px;font-size:4.6px;font-weight:600;color:#333}
</style>
</head>
<body>
<div class="page">

  <!-- benefits -->
  <section>
    <div class="abs product-photo" role="img" aria-label="Studio headphones resting on a chrome stand"></div>
    <h2 class="abs benefits-title">Benefits</h2>
    <h3 class="abs benefits-sub">LOREM IPSUM DOLOT SIR AMET</h3>
    <div class="abs benefits-copy">
      <p>Fusce sodales id mi sed vulputate. Pellentesque habitant morbi tristique senectus et netus et malesuada fames ac turpis egestas. Sed commodo at augue quis auctor.</p>
      <p>Proin non tincidunt enim. Vestibulum ante velit, laoreet at erat id, mollis molestie metus. Ut quam ligula, volutpat elementum pulvinar et, lacinia in ligula. Nunc consequat at ipsum ac porttitor.</p>
      <p>Suspendisse potenti. Etiam dignissim justo in arcu efficitur porttitor. Curabitur sed lectus vel ipsum hendrerit condimentum. Praesent et eros mi.</p>
      <p>Proin non tincidunt enim. Vestibulum ante velit, laoreet at erat id, mollis molestie metus. Ut quam ligula, volutpat elementum pulvinar et, lacinia in ligula. Nunc consequat at ipsum ac porttitor.</p>
      <p>Suspendisse potenti. Etiam dignissim justo in arcu efficitur porttitor. Curabitur sed lectus vel ipsum hendrerit condimentum. Praesent et eros mi.</p>
    </div>
    <a class="btn btn-read">Read More</a>
  </section>

  <!-- clients -->
  <section class="band" style="top:244px;height:108px;background:var(--band-grey)">
    <h2 class="abs center title" style="top:13px">They Already Trust Us</h2>
    <p class="abs center kicker" style="top:31px">A List Of Our Clients</p>
    <div class="client" style="left:130px;top:59px"><i class="dot"></i>TALVERN</div>
    <div class="client" style="left:201px;top:59px">intrant</div>
    <div class="client" style="left:273px;top:59px"><i class="dot"></i>NOVARE</div>
    <div class="client" style="left:343px;top:59px"><i class="dot"></i>MERITU</div>
    <div class="client" style="left:417px;top:59px">QUENO</div>
    <div class="client" style="left:484px;top:59px"><i class="dot"></i>DELOST</div>
  </section>

  <!-- certificates -->
  <section class="band" style="top:352px;height:132px;background:var(--band-warm)">
    <h2 class="abs center title" style="top:13px">We Are Quorvane &amp; Zelpix Certified</h2>
    <p class="abs center kicker" style="top:32px">Our Certificates</p>
  </section>
  <div class="badge" style="left:165px;background:var(--q-navy)"></div>
  <div class="badge" style="left:235px;background:var(--q-blue)"></div>
  <div class="badge" style="left:306px;background:var(--q-sky)"></div>
  <div class="badge" style="left:377px;background:var(--q-light)"></div>
  <div class="badge" style="left:448px;background:linear-gradient(180deg,var(--z-dark) 0 58%,var(--z-grey) 58%)"></div>

  <!-- contact -->
  <section>
    <h2 class="abs center title wide blue" style="top:491px">Say Hello</h2>
    <p class="abs center kicker" style="top:512px">Get In Touch</p>
    <div class="kick-rule" style="top:525px"></div>

    <div class="contact" style="left:114px">
      <svg width="9" height="9" viewBox="0 0 24 24"><path fill="var(--blue)" d="M6.6 10.8a15.2 15.2 0 0 0 6.6 6.6l2.2-2.2a1 1 0 0 1 1-.25 11.4 11.4 0 0 0 3.6.57 1 1 0 0 1 1 1V20a1 1 0 0 1-1 1A17 17 0 0 1 3 4a1 1 0 0 1 1-1h3.5a1 1 0 0 1 1 1c0 1.25.2 2.45.57 3.57a1 1 0 0 1-.25 1z"/></svg>
      <h3>Call Us At</h3>
      <p>212.555.0148</p>
    </div>
    <div class="contact" style="left:280px">
      <svg width="9" height="9" viewBox="0 0 24 24"><path fill="var(--blue)" d="M12 2a7 7 0 0 0-7 7c0 5.2 7 13 7 13s7-7.8 7-13a7 7 0 0 0-7-7zm0 9.5A2.5 2.5 0 1 1 12 6.5a2.5 2.5 0 0 1 0 5z"/></svg>
      <h3>Office Address</h3>
      <p>214 Harrow Ln # 12<br>Brookvale IL 60201<br>NY</p>
    </div>
    <div class="contact" style="left:442px">
      <svg width="9" height="9" viewBox="0 0 24 24"><path fill="var(--blue)" d="M2 5h20v2l-10 6L2 7z M2 9l10 6 10-6v10H2z"/></svg>
      <h3>Email Us At</h3>
      <p>info@lsgrp.com</p>
    </div>
  </section>

  <!-- chat form -->
  <section class="band" style="top:632px;height:166px;background:var(--band-soft)">
    <h2 class="abs center title wide" style="top:13px">Let’s Chat</h2>
    <p class="abs center kicker" style="top:33px">Fill Up The Forms To Send Queries</p>
    <div class="kick-rule" style="top:46px"></div>
  </section>
  <div class="field" style="left:136px;top:704px;width:200px;height:16px">Your Name</div>
  <div class="field" style="left:136px;top:726px;width:200px;height:16px">Your Email Id</div>
  <div class="field" style="left:344px;top:704px;width:200px;height:38px">Your Message</div>
  <a class="btn btn-submit">Submit</a>

  <!-- map -->
  <div class="abs map" role="img" aria-label="Street map of the office neighbourhood in lower Manhattan"></div>
  <svg class="abs" style="left:323px;top:869px" width="22" height="30" viewBox="0 0 22 30">
    <path d="M11 0a11 11 0 0 0-11 11c0 8 11 19 11 19s11-11 11-19A11 11 0 0 0 11 0z" fill="#2b2b2b"/>
    <circle cx="11" cy="11" r="5" fill="#fff"/><circle cx="11" cy="11" r="3" fill="#d7262e"/>
  </svg>

  <!-- social -->
  <section>
    <h2 class="abs center title wide" style="top:994px">Get Social</h2>
    <div class="social" style="left:198px"><div class="mark"></div><span>Friendly</span></div>
    <div class="social" style="left:256px"><div class="mark"></div><span>Chirper</span></div>
    <div class="social" style="left:313px"><div class="mark"></div><span>Linkwork</span></div>
    <div class="social" style="left:375px"><div class="mark"></div><span>Gathera</span></div>
    <div class="social" style="left:439px"><div class="mark"></div><span>Reelcast</span></div>
    <a class="btn btn-hello">SAY HELLO</a>
    <p class="abs center legal">© 2016, All Rights Reserved. Terms of Use &nbsp;|&nbsp; Privacy Policy</p>
    <div class="abs center brand"><div class="globe"></div><div class="name">LARKSPUR SYSTEMS GROUP</div></div>
    <p class="abs center to-top">GO TO TOP</p>
  </section>

</div>
</body>
</html>
```